Need home page concept design for existing website

Our existing website is www.nimbrel.com. We started re-branding project. We need one page (home page) concept made in Photoshop with a new theme. PLEASE REVIEW THE MOCK-UP OF NEW HOME PAGE IN THE ATTACHED MS DOC FILE.

We develop data processing productivity software for corporate clients. By purchasing our products and services our customers gain efficiency, cut cost, free up resources.

The new theme and styles should be modern responsive (compatible with mobile devices). Our current website's home page has lots of descriptive information which create a sense of clutter.

The new design should be clear and distinct. I like PixelHarbor.com color theme, font styles and menus. Another one I like http://velquora.com/ - the style, theme and the way they convey complicated idea to prospects.

Industry/Entity Type

Software

Font styles to use
Sans Serif

Requirements
Must have
• Clearness. Modern style. Responsive. Innovative business style that will convey new fresh approach to traditional problems our customers have. However it should not be too much extravagant, to scare off our corporate customers.

```html
<!DOCTYPE html>
<html lang="en">
<head>
<meta charset="utf-8">
<title>Nimbrel — Easy Productivity Solutions</title>
<link href="https://fonts.googleapis.com/css2?family=Oswald:wght@400;500&family=Open+Sans:wght@300;400;600;700&display=swap" rel="stylesheet">
<style>
:root{
  --blue:#1f78b8;
  --blue-dark:#17609a;
  --blue-light:#2e8fd0;
  --orange:#f36f21;
  --text:#555a5f;
  --text-dark:#3a3e42;
  --olive:#5d6150;
  --bg:#f8fafb;
  --band:#eef0f1;
  --footer:#2f3133;
  --footer-bottom:#26282a;
  --footer-text:#c9cbcd;
}
*{margin:0;padding:0;box-sizing:border-box}
html,body{width:787px;height:1200px;overflow:hidden}
body{font-family:'Open Sans',sans-serif;color:var(--text);background:var(--bg);position:relative}
.btn{position:absolute;display:flex;align-items:center;justify-content:center;color:#fff;font-family:'Oswald',sans-serif;font-weight:500;font-size:10px;letter-spacing:.2px;border-radius:2px;text-transform:uppercase}
.btn-orange{background:linear-gradient(#ff8a3a,#ee641a);border:1px solid #d95a14}
.btn-blue{background:linear-gradient(#2f8fd0,#1a6dab);border:1px solid #175f96}

.site-header{position:absolute;top:0;left:0;width:787px;height:59px;background:linear-gradient(#fff,#f1f3f4)}
.brand{position:absolute;left:104px;top:13px;font-weight:700;font-size:25px;color:var(--blue);letter-spacing:1px}
.tagline{position:absolute;left:239px;top:11px;height:34px;border-left:1px solid #d5d8da;padding-left:10px;font-size:7.5px;line-height:11px;color:#7a7e82;padding-top:5px}

.main-nav{position:absolute;top:59px;left:0;width:787px;height:33px;background:linear-gradient(#3a93cf,#1c6ba8);border-bottom:1px solid #155a8d}
.main-nav ul{list-style:none;display:flex;position:absolute;left:112px;top:0;height:33px;align-items:center}
.main-nav li{font-family:'Oswald',sans-serif;font-weight:500;font-size:10px;color:#fff;margin-right:21px;text-transform:uppercase}
.search{position:absolute;left:546px;top:6px;width:135px;height:19px;background:#fff;border:1px solid #0f4f80;font-size:7.5px;color:#888;padding:4px 5px}
.search svg{position:absolute;right:5px;top:4px}

.hero-photo{position:absolute;top:92px;left:0;width:787px;height:273px;background:linear-gradient(90deg,#cfd3d6 0%,#e2e5e7 25%,#eceeef 50%,#f3f4f5 70%,#e9ebed 100%)}
.hero-figure{position:absolute;top:92px;left:90px;width:285px;height:273px;background:radial-gradient(ellipse at 50% 40%,#c9cfd7 0%,#d7dbe0 55%,rgba(226,229,231,0) 75%)}
.hero-title{position:absolute;left:400px;top:126px;font-weight:300;font-size:21px;line-height:30px;color:var(--blue-dark)}
.hero-sub{position:absolute;left:400px;top:191px;font-weight:600;font-size:13px;color:var(--olive)}
.hero-text{position:absolute;left:401px;top:226px;width:295px;font-size:9.8px;line-height:15.5px;color:#6a6e62}
.hero-text b{font-weight:600;color:var(--olive)}

.video{position:absolute;left:107px;top:389px;width:277px;height:165px;background:linear-gradient(135deg,#8fa9c4,#c6d3e0 55%,#a9b9c9)}
.video-title{position:absolute;left:0;width:277px;top:52px;text-align:center;font-family:'Oswald',sans-serif;font-size:31px;color:#1b5f9e;letter-spacing:.5px}
.video-sub{position:absolute;left:0;width:277px;top:92px;text-align:center;font-style:italic;font-size:9px;color:#1f2a36}
.video-bar{position:absolute;left:0;bottom:0;width:277px;height:10px;background:#1c1c1c}
.video-progress{position:absolute;left:0;bottom:10px;width:277px;height:2px;background:#555}
.video-progress i{display:block;width:12px;height:2px;background:#d22}
.overview-title{position:absolute;left:413px;top:387px;font-weight:300;font-size:15px;color:var(--text-dark)}
.overview-text{position:absolute;left:413px;top:429px;width:285px;font-size:10px;line-height:15.5px;color:var(--text)}
.overview-text p{margin-bottom:15px}
.link{font-family:'Oswald',sans-serif;font-size:10px;color:var(--blue);text-decoration:underline}

.sector{position:absolute;top:580px;display:flex;align-items:center}
.sector .ico{width:36px;height:36px;border-radius:50%;background:linear-gradient(#fff,#e7eaec);border:1px solid #dde1e4;display:flex;align-items:center;justify-content:center;margin-right:9px}
.sector span{font-size:10.5px;line-height:15.5px;color:#5a5e62}

.promo{position:absolute;top:639px;width:283px;height:107px;background:linear-gradient(120deg,#1a73b6 0%,#1b7cc1 55%,#2a8bcc 56%,#1a6cab 100%);color:#fff}
.promo .pic{position:absolute;left:16px;top:18px;width:70px;height:70px;border-radius:50%;background:radial-gradient(circle at 45% 40%,#e9edf0,#a9b7c4);border:2px solid #fff}
.promo h3{position:absolute;left:98px;top:17px;font-size:10.5px;font-weight:700;letter-spacing:.3px}
.promo p{position:absolute;left:98px;top:42px;width:172px;font-size:7.8px;line-height:12.4px}

.events-title{position:absolute;left:107px;top:767px;font-weight:300;font-size:16px;color:#6a6e72;display:flex;align-items:center}
.events-title svg{margin-right:6px}
.events-links{position:absolute;left:488px;top:777px;font-family:'Oswald',sans-serif;font-size:9.5px;color:#6d7175}
.events-links .sep{margin:0 20px;color:#aaa}
.rule{position:absolute;top:799px;height:1px;background:#d9dcde}
.event{position:absolute;top:811px;width:283px}
.event h4{font-size:10px;font-weight:700;color:var(--text-dark)}
.event h4 span{color:#6a6e72;font-weight:600}
.event p{margin-top:12px;font-size:7px;line-height:11px;color:#6a6e72}
.event .date{position:absolute;top:71px;left:0;font-size:7.5px;color:#6a6e72;display:flex;align-items:center}
.event .date svg{margin-right:5px}

.signup{position:absolute;top:920px;left:0;width:787px;height:55px;background:var(--band);border-top:1px solid #e3e5e7}
.signup h2{position:absolute;left:142px;top:18px;font-size:14.5px;font-weight:600;color:#8a8e92}
.signup h2 em{font-style:normal;color:var(--orange)}
.signup .field{position:absolute;left:363px;top:14px;width:214px;height:24px;background:#fff;border:1px solid #d8dbdd;font-size:7.5px;color:#8a8e92;padding:7px 10px}

.site-footer{position:absolute;top:975px;left:0;width:787px;height:185px;background:var(--footer)}
.footer-brand{position:absolute;left:105px;top:71px;font-weight:700;font-size:20px;color:var(--blue-light);letter-spacing:1px}
.footer-col{position:absolute;top:24px}
.footer-col h5{font-size:8.5px;font-weight:400;color:#b5b8bb;text-transform:uppercase;letter-spacing:.3px;margin-bottom:13px}
.footer-nav li{list-style:none;font-size:7.5px;color:#fff;height:20.3px;display:flex;align-items:flex-start}
.footer-nav li::before{content:"";width:0;height:0;border-left:3px solid var(--blue-light);border-top:3px solid transparent;border-bottom:3px solid transparent;margin:2px 6px 0 0}
.post{font-size:7.5px;line-height:12px;color:var(--footer-text);width:122px}
.post .meta{font-size:5.5px;color:#8d9093;margin-bottom:1px}
.post .ttl{color:var(--blue-light)}
.post-sep{width:122px;height:2px;background:#45484b;margin:8px 0 10px}
.contacts{font-size:7.5px;line-height:12.3px;color:var(--footer-text)}
.contacts p{margin-bottom:12px}
.footer-bottom{position:absolute;top:1160px;left:0;width:787px;height:40px;background:var(--footer-bottom);font-size:7px;color:#8d9093}
.footer-bottom .copy{position:absolute;left:95px;top:15px}
.footer-bottom .legal{position:absolute;left:528px;top:15px}
</style>
</head>
<body>

<header class="site-header">
  <div class="brand">NIMBREL</div>
  <div class="tagline">Easy Productivity Solutions for<br>Managing Your Ordana ERP Data</div>
  <div class="btn btn-blue" style="left:498px;top:14px;width:86px;height:27px">Request a Quote</div>
  <div class="btn btn-orange" style="left:596px;top:14px;width:86px;height:27px">Get a Free Trial</div>
</header>

<nav class="main-nav">
  <ul>
    <li>Home</li><li>Data Loaders</li><li>Web Solutions</li><li>Output Solutions</li><li>About</li><li>Contact</li>
  </ul>
  <div class="search">Search
    <svg width="10" height="10" viewBox="0 0 10 10"><circle cx="4" cy="4" r="3" fill="none" stroke="#444" stroke-width="1.3"/><line x1="6.2" y1="6.2" x2="9" y2="9" stroke="#444" stroke-width="1.5"/></svg>
  </div>
</nav>

<section class="hero">
  <div class="hero-photo" role="img" aria-label="Blurred bright office interior background"></div>
  <div class="hero-figure" role="img" aria-label="Smiling businesswoman in glasses and striped shirt working at a laptop"></div>
  <h1 class="hero-title">Quickly and Safely Manage<br>Complex Ordana Tasks</h1>
  <div class="hero-sub">Significantly Increase Efficiency</div>
  <p class="hero-text">Don't get bogged down by cumbersome Ordana ERP tasks when <b>Nimbrel's easy-to-use, safe and simple</b> solutions can <b>triple</b> your productivity.</p>
  <div class="btn btn-orange" style="left:399px;top:292px;width:86px;height:27px">Get a Free Trial</div>
</section>

<section class="overview">
  <div class="video" role="img" aria-label="Video still of colleagues reviewing work at a desk">
    <div class="video-title">DATA LOADER</div>
    <div class="video-sub">Productivity Solutions for Ordana ERP</div>
    <div class="video-progress"><i></i></div>
    <div class="video-bar"></div>
  </div>
  <h2 class="overview-title">Overview</h2>
  <div class="overview-text">
    <p>Download your Ordana ERP data into easy-to-use Sheetora spread-sheets where you can make massive changes and upload them safely to back Ordana.</p>
    <p>Find out more about what makes Data Loaders the perfect solu-tion for Ordana data management!</p>
    <span class="link">Learn More</span>
  </div>

  <div class="sector" style="left:107px">
    <div class="ico"><svg width="16" height="16" viewBox="0 0 16 16"><circle cx="8" cy="8" r="6.5" fill="none" stroke="#1f78b8" stroke-width="1.5"/><text x="8" y="11.3" font-size="9" font-weight="700" text-anchor="middle" fill="#1f78b8" font-family="Open Sans,sans-serif">$</text></svg></div>
    <span>Finance</span>
  </div>
  <div class="sector" style="left:255px">
    <div class="ico"><svg width="16" height="14" viewBox="0 0 16 14"><g fill="#1f78b8"><rect x="2" y="5" width="2" height="6"/><rect x="5" y="2" width="2" height="9"/><rect x="8" y="4" width="2" height="7"/><rect x="11" y="6" width="2" height="5"/><rect x="0" y="12" width="16" height="1.5"/></g></svg></div>
    <span>Master Data &amp;<br>Inventory</span>
  </div>
  <div class="sector" style="left:400px">
    <div class="ico"><svg width="18" height="14" viewBox="0 0 18 14"><g fill="none" stroke="#1f78b8" stroke-width="1.3"><circle cx="5" cy="7" r="4" fill="#1f78b8"/><path d="M9 7h3M12 2v10M12 2h3M12 7h3M12 12h3"/></g></svg></div>
    <span>Distribution &amp;<br>Supply Chain</span>
  </div>
  <div class="sector" style="left:548px">
    <div class="ico"><svg width="16" height="14" viewBox="0 0 16 14"><g fill="#1f78b8" stroke="#1f78b8" stroke-width="1.2"><path d="M2 11L6 7L9 9L14 3" fill="none"/><circle cx="2" cy="11" r="1.6"/><circle cx="6" cy="7" r="1.6"/><circle cx="9" cy="9" r="1.6"/><circle cx="14" cy="3" r="1.6"/></g></svg></div>
    <span>Production</span>
  </div>

  <article class="promo" style="left:105px">
    <div class="pic" role="img" aria-label="Hands using a laptop and tablet on a desk"></div>
    <h3>WEB SOLUTIONS</h3>
    <p>Access Ordana ERP data from anywhere on any mobile device to check inventory, purchase orders and more. For both Ordana users and non-users.</p>
  </article>
  <article class="promo" style="left:400px">
    <div class="pic" role="img" aria-label="Business team reviewing printed documents"></div>
    <h3>OUTPUT SOLUTIONS</h3>
    <p>From outputting easy information-sharing documents to dynamic print solutions, Nimbrel output solutions for Ordana ERP greatly improve your efficiency.</p>
  </article>
</section>

<section class="events">
  <h2 class="events-title"><svg width="13" height="13" viewBox="0 0 13 13"><rect x="1" y="2.5" width="11" height="9.5" fill="none" stroke="#6a6e72" stroke-width="1.2"/><rect x="1" y="2.5" width="11" height="2.5" fill="#6a6e72"/><rect x="3.5" y="0.5" width="1.3" height="3" fill="#6a6e72"/><rect x="8.2" y="0.5" width="1.3" height="3" fill="#6a6e72"/></svg>Upcoming Events</h2>
  <div class="events-links"><u>View Past Webinars</u><span class="sep">|</span><u>Request a Webinar</u></div>
  <div class="rule" style="left:105px;width:283px"></div>
  <div class="rule" style="left:400px;width:283px"></div>

  <article class="event" style="left:105px">
    <h4><span>WEBINARS:</span> Transforming Your Fiscal EOY Process</h4>
    <p>The point of using Lorem Ipsum is that it has a more-or-less normal distribution of letters, as opposed to using 'Content here, content here'.</p>
    <div class="date"><svg width="7" height="7" viewBox="0 0 7 7"><rect x=".5" y="1" width="6" height="5.5" fill="none" stroke="#888"/><rect x=".5" y="1" width="6" height="1.5" fill="#888"/></svg>8 December 2013</div>
    <div class="btn btn-orange" style="left:215px;top:59px;width:68px;height:24px;font-family:'Open Sans',sans-serif;font-weight:600;font-size:9px;text-transform:none">Register</div>
  </article>
  <article class="event" style="left:399px">
    <h4><span>WEBINARS:</span> Transforming Your Fiscal EOY Process</h4>
    <p>The point of using Lorem Ipsum is that it has a more-or-less normal distribution of letters, as opposed to using 'Content here, content here'.</p>
    <div class="date"><svg width="7" height="7" viewBox="0 0 7 7"><rect x=".5" y="1" width="6" height="5.5" fill="none" stroke="#888"/><rect x=".5" y="1" width="6" height="1.5" fill="#888"/></svg>8 December 2013</div>
    <div class="btn btn-orange" style="left:215px;top:59px;width:68px;height:24px;font-family:'Open Sans',sans-serif;font-weight:600;font-size:9px;text-transform:none">Register</div>
  </article>
</section>

<section class="signup">
  <h2>SIGN UP FOR <em>FREE</em> WEBINARS</h2>
  <div class="field">Enter Your Email Address</div>
  <div class="btn btn-blue" style="left:577px;top:14px;width:67px;height:24px;font-family:'Open Sans',sans-serif;font-weight:600;font-size:9px;text-transform:none">Submit</div>
</section>

<footer class="site-footer">
  <div class="footer-brand">NIMBREL</div>
  <div class="footer-col" style="left:252px">
    <h5>Navigation</h5>
    <ul class="footer-nav"><li>Home</li><li>Date Loaders</li><li>Web Solutions</li><li>Output Solutions</li><li>About</li><li>Contact</li></ul>
  </div>
  <div class="footer-col" style="left:399px">
    <h5>Recent Posts</h5>
    <div class="post"><div class="meta">DEC 15, 2012 &nbsp;|&nbsp; BY ADMIN</div><div class="ttl">Morbi a libero eget erat auctor</div>Sus vitae id tortor suspendisse. Vestibulum eu ligula lorem ...</div>
    <div class="post-sep"></div>
    <div class="post"><div class="meta">DEC 15, 2012 &nbsp;|&nbsp; BY ADMIN</div><div class="ttl">Morbi a libero eget erat auctor</div>Sus vitae id tortor suspendisse. Vestibulum eu ligula lorem ...</div>
  </div>
  <div class="footer-col contacts" style="left:547px">
    <h5>Contacts</h5>
    <p>Larkfield Inc.<br>PO Box 40219<br>Garnet Lane, Redhaven<br>Westmoor 7042 Calvoria</p>
    <p>Phone: (555) 010-4417<br>Fax: (555) 010-4418</p>
    <p>support@nimbrel.com</p>
  </div>
</footer>
<div class="footer-bottom">
  <span class="copy">Copyright © 2014 Nimbrel. All Rights Reserved.</span>
  <span class="legal">Site Map &nbsp;|&nbsp; Privacy Policy &nbsp;|&nbsp; Contact Us</span>
</div>

</body>
</html>
```